Property developer, money partner needs business card design using logo concept provided

Our company develops residential properties, does money lends for joint ventures in property deals and finds property deals for other money partners. We have provided a basic logo for you to work from. Any graphic or logo design on the card is to communicate development and finance collaboration. Color choice is not so important for us, but color choice does need to reflect professionalism.

```html
<!DOCTYPE html>
<html lang="en">
<head>
<meta charset="utf-8">
<title>Brightgate Property Solutions – Business Card</title>
<link href="https://fonts.googleapis.com/css2?family=Arimo:wght@400;700&display=swap" rel="stylesheet">
<style>
  :root {
    --stage: #2f2f31;
    --card: #242426;
    --card-edge: #3a3a3d;
    --brand-blue: #1f7fd1;
    --text-light: #f2f2f2;
    --text-muted: #c9c9cc;
    --divider: #5a5a5e;
  }
  * { margin: 0; padding: 0; box-sizing: border-box; }
  html, body { width: 1200px; height: 689px; overflow: hidden; background: var(--stage); }
  body { font-family: "Arimo", Arial, sans-serif; position: relative; }

  .card {
    position: absolute;
    top: 201px;
    width: 500px;
    height: 286px;
    background: var(--card);
    border: 1px solid var(--card-edge);
    border-radius: 16px;
    overflow: hidden;
  }
  .card--front { left: 60px; }
  .card--back { left: 640px; }

  .brand {
    position: absolute;
    display: flex;
    flex-direction: column;
    align-items: center;
    text-align: center;
    color: var(--text-light);
  }
  .card--front .brand { left: 0; right: 0; top: 88px; }
  .card--back .brand { left: 0; width: 250px; top: 88px; }

  .brand__mark {
    width: 44px; height: 44px;
    border-radius: 50%;
    background: var(--brand-blue);
    margin-bottom: 14px;
  }
  .brand__name {
    font-size: 26px;
    font-weight: 700;
    letter-spacing: 3px;
    text-transform: uppercase;
  }
  .brand__tagline {
    margin-top: 6px;
    font-size: 13px;
    letter-spacing: 2px;
    color: var(--text-muted);
  }
  .brand__reg {
    margin-top: 4px;
    font-size: 9px;
    letter-spacing: 1.5px;
    color: var(--text-muted);
  }

  .divider {
    position: absolute;
    left: 250px; top: 30px;
    width: 1px; height: 226px;
    background: linear-gradient(to bottom, transparent, var(--divider) 20%, var(--divider) 80%, transparent);
  }

  .contact {
    position: absolute;
    left: 276px; top: 40px;
    color: var(--text-light);
  }
  .contact__name { font-size: 20px; font-weight: 700; color: var(--brand-blue); }
  .contact__role { font-size: 12px; margin-top: 3px; }
  .contact__address { font-size: 12px; line-height: 17px; margin-top: 22px; }
  .contact__list { list-style: none; margin-top: 20px; font-size: 12px; }
  .contact__item { display: flex; align-items: center; gap: 8px; height: 19px; }
  .contact__icon { width: 11px; height: 11px; fill: var(--brand-blue); flex: none; }
</style>
</head>
<body>
  <section class="card card--front" aria-label="Card front">
    <div class="brand">
      <span class="brand__mark"></span>
      <span class="brand__name">Brightgate</span>
      <span class="brand__tagline">Property Solutions</span>
      <span class="brand__reg">A.C.N 481 203 769</span>
    </div>
  </section>

  <section class="card card--back" aria-label="Card back">
    <div class="brand">
      <span class="brand__mark"></span>
      <span class="brand__name">Brightgate</span>
      <span class="brand__tagline">Property Solutions</span>
      <span class="brand__reg">A.C.N 481 203 769</span>
    </div>

    <div class="divider"></div>

    <div class="contact">
      <p class="contact__name">Daniel Morrow</p>
      <p class="contact__role">Managing Director</p>
      <p class="contact__address">412 Cedar Ridge Road<br>Fairbanks, Alaska 99701</p>
      <ul class="contact__list">
        <li class="contact__item">
          <svg class="contact__icon" viewBox="0 0 12 12"><path d="M2.5 0.5l2 2.5-1.2 1.3c.7 1.6 2 2.9 3.6 3.6l1.3-1.2 2.5 2-1.2 2.3C4.8 10.8 1.2 7.2.3 1.7z"/></svg>
          555-210-4187
        </li>
        <li class="contact__item">
          <svg class="contact__icon" viewBox="0 0 12 12"><path d="M3 0h6a1 1 0 0 1 1 1v10a1 1 0 0 1-1 1H3a1 1 0 0 1-1-1V1a1 1 0 0 1 1-1zm.5 1.5v8h5v-8z"/></svg>
          555-318-2064
        </li>
        <li class="contact__item">
          <svg class="contact__icon" viewBox="0 0 12 12"><path d="M0 2h12v8H0zm1 1v.4l5 3.2 5-3.2V3zm0 1.6V9h10V4.6L6 7.8z"/></svg>
          info@brightgatehomes.com
        </li>
        <li class="contact__item">
          <svg class="contact__icon" viewBox="0 0 12 12"><circle cx="6" cy="6" r="6"/></svg>
          www.brightgatehomes.com
        </li>
      </ul>
    </div>
  </section>
</body>
</html>
```